StoneBay construction business cards

I need a business card with a replacement window photo or graphic on it .phone # 919 482 -7316 stonebayconstruction@mailfort.net fax #919 274-8093 '' The Window Replacement Specialist"

Industry/Entity Type

Construction

```html
<!DOCTYPE html>
<html lang="en">
<head>
<meta charset="utf-8">
<title>StoneBay Construction – Business Cards</title>
<link rel="stylesheet" href="https://fonts.googleapis.com/css2?family=Oswald:wght@600&family=Encode+Sans+Condensed:wght@700&family=Roboto+Condensed:wght@300;400&display=swap">
<style>
  :root {
    --brand-green: #5bbf14;
    --ink: #2b2b2b;
    --paper: #ffffff;
    --canvas: #ececec;
    --glass-light: #fbfbfb;
    --glass-mid: #e9ecee;
    --frame-shadow: rgba(0,0,0,0.12);
  }
  * { box-sizing: border-box; margin: 0; padding: 0; }
  html, body { width: 1080px; height: 1200px; overflow: hidden; background: var(--canvas); }
  .canvas { position: relative; width: 1080px; height: 1200px; }

  .card {
    position: absolute; width: 815px; height: 478px; overflow: hidden;
    box-shadow: 0 4px 14px var(--frame-shadow);
  }

  /* Front */
  .card--front { left: 127px; top: 93px; background: var(--paper); }
  .front__band { position: absolute; left: 0; top: 0; width: 100%; height: 150px; background: var(--brand-green); }
  .front__photo {
    position: absolute; left: 0; top: 150px; width: 100%; height: 328px;
    background: linear-gradient(180deg, var(--glass-light) 0%, var(--glass-mid) 70%, #dcdfe1 100%);
  }
  .front__wordmark {
    position: absolute; left: 0; right: 0; top: 182px; text-align: center;
    font-family: "Oswald", sans-serif; font-weight: 600; color: var(--brand-green);
    font-size: 84px; line-height: 1; letter-spacing: 1px;
  }
  .front__wordmark-sub {
    position: absolute; left: 0; right: 0; top: 282px; text-align: center;
    font-family: "Oswald", sans-serif; font-weight: 600; color: var(--brand-green);
    font-size: 30px; letter-spacing: 6px;
  }
  .front__tagline {
    position: absolute; left: 0; right: 0; top: 372px; text-align: center;
    font-family: "Encode Sans Condensed", sans-serif; font-weight: 700;
    font-size: 23px; color: var(--brand-green);
  }

  /* Back */
  .card--back { left: 124px; top: 638px; background: var(--brand-green); }
  .back__panel {
    position: absolute; left: 42px; top: 34px; width: 722px; height: 399px;
    background: var(--paper);
  }
  .back__window {
    position: absolute; top: 15px; width: 150px; height: 370px;
    background: linear-gradient(90deg, #f4f4f4 0%, #e2e4e6 50%, #f7f7f7 100%);
    border: 2px solid #d7d9db;
  }
  .back__window--left { left: 0; }
  .back__window--right { right: 0; }
  .back__wordmark {
    position: absolute; left: 0; right: 0; top: 72px; text-align: center;
    font-family: "Oswald", sans-serif; font-weight: 600; color: var(--brand-green);
    font-size: 34px; line-height: 1;
  }
  .back__wordmark-sub {
    position: absolute; left: 0; right: 0; top: 112px; text-align: center;
    font-family: "Oswald", sans-serif; font-weight: 600; color: var(--brand-green);
    font-size: 13px; letter-spacing: 3px;
  }
  .contact-list {
    position: absolute; left: 205px; top: 164px; list-style: none;
    font-family: "Roboto Condensed", sans-serif; font-weight: 400;
    font-size: 22px; color: var(--ink);
  }
  .contact-list li { display: flex; align-items: flex-start; gap: 8px; height: 40px; }
  .contact-list li.contact--address { height: auto; line-height: 30px; }
  .contact-icon { width: 22px; height: 22px; flex: none; margin-top: 3px; }
</style>
</head>
<body>
<main class="canvas">

  <section class="card card--front" aria-label="Business card front">
    <div class="front__band"></div>
    <div class="front__photo" role="img" aria-label="Photo of a bright white bay window with replacement frames"></div>
    <div class="front__wordmark">StoneBay</div>
    <div class="front__wordmark-sub">CONSTRUCTION</div>
    <p class="front__tagline">The Window Replacement Specialist</p>
  </section>

  <section class="card card--back" aria-label="Business card back">
    <div class="back__panel">
      <div class="back__window back__window--left" role="img" aria-label="Photo of an opened white window sash, left side"></div>
      <div class="back__window back__window--right" role="img" aria-label="Photo of an opened white window sash, right side"></div>

      <div class="back__wordmark">StoneBay</div>
      <div class="back__wordmark-sub">CONSTRUCTION</div>

      <ul class="contact-list">
        <li>
          <svg class="contact-icon" viewBox="0 0 22 22" aria-hidden="true"><rect x="5" y="1" width="12" height="20" rx="2" fill="none" stroke="#5bbf14" stroke-width="2"/><rect x="9" y="17" width="4" height="1.6" fill="#5bbf14"/></svg>
          <span>919 482 7316</span>
        </li>
        <li>
          <svg class="contact-icon" viewBox="0 0 22 22" aria-hidden="true"><rect x="1" y="5" width="20" height="13" fill="none" stroke="#5bbf14" stroke-width="2"/><path d="M1 5 L11 13 L21 5" fill="none" stroke="#5bbf14" stroke-width="2"/></svg>
          <span>stonebayconstruction@mailfort.net</span>
        </li>
        <li>
          <svg class="contact-icon" viewBox="0 0 22 22" aria-hidden="true"><rect x="5" y="2" width="12" height="7" fill="none" stroke="#5bbf14" stroke-width="2"/><rect x="1" y="9" width="20" height="9" fill="#5bbf14"/><rect x="5" y="14" width="12" height="6" fill="#fff" stroke="#5bbf14" stroke-width="1.5"/></svg>
          <span>919 274-8093</span>
        </li>
        <li class="contact--address">
          <svg class="contact-icon" viewBox="0 0 22 22" aria-hidden="true"><path d="M1 10 L11 2 L21 10 Z" fill="#5bbf14"/><rect x="3" y="10" width="16" height="10" fill="#5bbf14"/><rect x="9" y="13" width="4" height="7" fill="#fff"/></svg>
          <span>218 Millbrook Lane,<br>Ashford North Carolina 27604</span>
        </li>
      </ul>
    </div>
  </section>

</main>
</body>
</html>
```